Brookmere Osteopathy and dry needling business card

Business card for Brookmere Osteopathy and Dry Needling.

Industry/Entity Type

Health

Contact Information for Business Card

I do not have a phone number yet. I also do not have an email address yet. The physical address is: 47 Lindcombe Lane Brookmere The website is: www.brookmereosteopathyclinic.example My details are: Dr Marcus Penhallow, Osteopath (B.Clin.Sci (Ost) M.Ost BSC ECON (Hons)

Colors
0094D4
00A9DD
6FCCEA
C7EBF8
E9F6FB

Requirements
Must have
• logo on the back
Nice to have
• Maybe a space for me to write an appointment time and date on the card.

```html
<!DOCTYPE html>
<html lang="en">
<head>
<meta charset="utf-8">
<title>Brookmere Osteopathy and Dry Needling – Business Card</title>
<link href="https://fonts.googleapis.com/css2?family=Montserrat:wght@400;600;700&display=swap" rel="stylesheet">
<style>
  :root {
    --brand-blue: #0E90CB;
    --accent-orange: #F18A21;
    --paper-white: #F3F3F2;
    --stage: #232323;
    --text-light: #FFFFFF;
  }
  * { box-sizing: border-box; margin: 0; padding: 0; }
  html, body {
    width: 1200px; height: 1059px; overflow: hidden;
    background: var(--stage);
    font-family: "Montserrat", sans-serif;
  }
  .canvas { position: relative; width: 1200px; height: 1059px; }
  .card {
    position: absolute; left: 255px; width: 690px; height: 392px;
    border-radius: 18px; overflow: hidden; background: var(--brand-blue);
  }
  .card--front { top: 89px; }
  .card--back { top: 546px; }
  .card__shape { position: absolute; inset: 0; width: 100%; height: 100%; }

  .brand-mark {
    position: absolute; border-radius: 50%;
    display: flex; align-items: center; justify-content: center; text-align: center;
    font-weight: 600; letter-spacing: 0.06em; text-transform: uppercase; line-height: 1.35;
  }
  .card--front .brand-mark {
    left: 471px; top: 40px; width: 176px; height: 176px;
    border: 2px solid var(--brand-blue); color: var(--brand-blue); font-size: 14px;
  }
  .card--back .brand-mark {
    left: 228px; top: 79px; width: 234px; height: 234px;
    border: 2px solid var(--text-light); color: var(--text-light); font-size: 18px;
  }

  .practitioner { position: absolute; left: 37px; top: 214px; color: var(--text-light); }
  .practitioner__name {
    color: var(--accent-orange); font-weight: 700; font-size: 21.5px;
    text-transform: uppercase; letter-spacing: 0.01em; margin-bottom: 4px;
  }
  .practitioner__credentials { font-size: 15.5px; line-height: 21px; font-weight: 400; }

  .contact { position: absolute; left: 37px; top: 300px; list-style: none; color: var(--text-light); }
  .contact__item { display: flex; align-items: center; gap: 8px; font-size: 16px; height: 29px; }
  .contact__icon { width: 14px; height: 14px; flex: none; }
</style>
</head>
<body>
<main class="canvas">

  <section class="card card--front" aria-label="Business card front">
    <svg class="card__shape" viewBox="0 0 690 392" preserveAspectRatio="none" aria-hidden="true">
      <path d="M216,0 C262,222 455,334 664,330 L690,330 L690,0 Z" fill="#FFFFFF"/>
      <path d="M219,0 C265,220 457,332 664,329 L690,328 L690,0 Z" fill="var(--accent-orange)"/>
      <path d="M244,0 C290,212 472,330 690,328 L690,0 Z" fill="var(--paper-white)"/>
    </svg>

    <div class="brand-mark">Brookmere<br>Osteopathy</div>

    <div class="practitioner">
      <h1 class="practitioner__name">Dr Marcus Penhallow</h1>
      <p class="practitioner__credentials">Osteopath (B.Clin.Sci (Ost)<br>M.Ost BSC ECON (Hons)</p>
    </div>

    <ul class="contact">
      <li class="contact__item">
        <svg class="contact__icon" viewBox="0 0 16 16" aria-hidden="true">
          <g fill="none" stroke="var(--accent-orange)" stroke-width="1.3">
            <circle cx="8" cy="8" r="7"/>
            <ellipse cx="8" cy="8" rx="3.2" ry="7"/>
            <line x1="1" y1="8" x2="15" y2="8"/>
            <line x1="2.2" y1="4.5" x2="13.8" y2="4.5"/>
            <line x1="2.2" y1="11.5" x2="13.8" y2="11.5"/>
          </g>
        </svg>
        www.brookmereosteopathyclinic.example
      </li>
      <li class="contact__item">
        <svg class="contact__icon" viewBox="0 0 16 16" aria-hidden="true">
          <path d="M8 0.8C4.9 0.8 2.6 3.1 2.6 6.1 2.6 10 8 15.4 8 15.4S13.4 10 13.4 6.1C13.4 3.1 11.1 0.8 8 0.8Z" fill="var(--accent-orange)"/>
          <circle cx="8" cy="6" r="2.1" fill="var(--brand-blue)"/>
        </svg>
        47 Lindcombe Lane Brookmere
      </li>
    </ul>
  </section>

  <section class="card card--back" aria-label="Business card back">
    <div class="brand-mark">Brookmere<br>Osteopathy</div>
  </section>

</main>
</body>
</html>
```